High profile consultancy

We need a web design for a company called BK Services. BK as abbreviation for Bold Keystone.

Company focusses on Sourcing (BK Sourcing, focus on ICT), Metrics (BK Metrics; focus on business case analysis and trends in ICT) and Software (BK software; to be developed later on; mainly tools supporting BK soucing and metrics)

Customers base consists of large enterprises, >1000 employees.

Site needs to have menu's for
- services
- login
- about
and a special area ' inspire ' to be able to communicate topics that should inspire our customers to contact us.

but key; it schould communicate our expertise and focus on deep knowlegde of ICT sourcing

Reason: please advice on content management systems to be used to maintain site also please advice on Trovix search clickbids. Will provide feedback on designs shortly.

Target Market(s)

CIO's; board of directors;
company excels in ICT / business knowledge and ability to execute; creates / optimizes relations between ICT suppliers and enterprises.

Requirements
Must have
• website should be easily be found; adaptive by design; accessible by all browsers.
• Need to have a login section for later use
Nice to have
• usage of (draft) logo. see upload.

```html
<!DOCTYPE html>
<html lang="en">
<head>
<meta charset="utf-8">
<title>BK Services</title>
<link href="https://fonts.googleapis.com/css2?family=Arimo:ital,wght@0,400;0,700;1,400&display=swap" rel="stylesheet">
<style>
:root{
  --page:#efefef;
  --white:#ffffff;
  --brand:#0b6ab8;
  --brand-dark:#0a4f8c;
  --title-blue:#1d5b9e;
  --call-blue:#1a7bbf;
  --events-red:#a8071a;
  --testimonial-grey:#4a4a4a;
  --news-bg:#c9e1f5;
  --news-label:#e6f1fb;
  --text:#2b2b2b;
  --line:#dcdcdc;
  --accent:#f08c00;
}
*{box-sizing:border-box;margin:0;padding:0}
html,body{width:1200px;height:1152px;overflow:hidden}
body{background:var(--page);font-family:"Arimo",Arial,sans-serif;color:var(--text);position:relative}
.sheet{position:absolute;left:112px;top:0;width:975px;height:936px;background:var(--white);box-shadow:0 0 4px rgba(0,0,0,.12)}
.logo{position:absolute;display:flex;align-items:center;gap:10px}
.logo-dot{width:40px;height:40px;border-radius:50%;background:var(--brand)}
.logo-name{font-size:30px;font-weight:700;color:var(--brand-dark);letter-spacing:.5px}
.site-logo{left:27px;top:28px}
.account{position:absolute;right:26px;top:27px;display:flex;gap:6px}
.account a{display:flex;align-items:center;gap:5px;height:24px;padding:0 9px;border-radius:3px;background:linear-gradient(#555,#2e2e2e);color:#fff;font-size:13px;text-decoration:none;border:1px solid #222}
.call{position:absolute;right:26px;top:66px;font-size:16px;font-weight:700;color:#111}
.call span{color:var(--call-blue)}
.nav{position:absolute;left:27px;top:108px;width:923px;height:36px;background:var(--brand);display:flex}
.nav a{color:#fff;text-decoration:none;font-size:14px;padding:0 8px;line-height:36px;border-right:1px solid rgba(255,255,255,.18)}
.nav a:first-child{padding-left:15px}
.nav a:last-child{border-right:0}
.hero{position:absolute;left:27px;top:144px;width:923px;height:357px;overflow:hidden}
.hero-photo{position:absolute;inset:0;background:linear-gradient(90deg,#e6e8ea 0%,#cfd7de 35%,#dfe3e6 60%,#c9ccd0 78%,#e9ebee 100%)}
.hero-tag{position:absolute;left:0;top:128px;width:228px;height:99px;background:rgba(44,66,44,.78);border-bottom:4px solid #2a3a28;padding:24px 0 0 30px;color:#fff}
.hero-tag h2{font-size:22px;font-weight:700;letter-spacing:.3px}
.hero-tag p{font-size:16px;margin-top:5px}
.wheel{position:absolute;left:313px;top:37px;width:278px;height:278px;border-radius:50%;background:radial-gradient(circle,#ffffff 0 22%,#c9a070 45%,#6f7a48 70%,#5c7fc0 100%)}
.news{position:absolute;left:27px;top:510px;width:923px;height:36px;background:var(--news-bg);font-size:12px;color:#1f4c7f}
.news-label{position:absolute;left:0;top:0;height:36px;width:68px;background:var(--news-label);font-size:17px;font-weight:700;color:var(--title-blue);line-height:36px;padding-left:14px}
.news-label::after{content:"";position:absolute;right:-18px;top:0;border-left:18px solid var(--news-label);border-top:18px solid transparent;border-bottom:18px solid transparent}
.news-text{position:absolute;left:98px;top:12px}
.news-arrows{position:absolute;right:8px;top:11px;display:flex;gap:3px}
.news-arrows span{width:14px;height:14px;background:#fff;border:1px solid #aac;font-size:10px;line-height:12px;text-align:center;color:#333}
.service{position:absolute;top:558px;width:298px;height:103px;border:1px solid var(--line);background:#fff}
.service-art{position:absolute;left:22px;top:20px;width:66px;height:66px}
.service h3{position:absolute;left:100px;top:24px;font-size:18px;color:var(--title-blue)}
.service p{position:absolute;left:100px;top:51px;width:190px;font-size:12px;line-height:17px;color:#333}
.panel{position:absolute;top:675px;width:298px;height:240px}
.panel-head{height:34px;color:#fff;font-size:18px;font-weight:700;line-height:34px;padding-left:17px;position:relative}
.panel-head svg{position:absolute;right:10px;top:5px}
.panel-body{height:206px;border:1px solid var(--line);border-top:0;background:linear-gradient(#fff 60%,#f1f1f1);padding:10px 10px 10px 17px;font-size:12px;line-height:22px;color:#222}
.panel-body p+p{margin-top:8px}
.date{color:var(--brand)}
.more,.who{color:var(--accent);font-style:italic}
.footer-logo{left:120px;top:960px;gap:8px}
.footer-logo .logo-dot{background:#777;width:32px;height:32px}
.footer-logo .logo-name{color:#666;font-size:20px}
.fcol{position:absolute;top:936px;height:147px;border-left:1px solid var(--line);padding:20px 0 0 26px}
.fcol h4{font-size:14px;color:#555;margin-bottom:8px}
.fcol a{display:block;font-size:12px;color:#555;text-decoration:none;line-height:22px;letter-spacing:.5px}
.social a{display:flex;align-items:center;gap:9px;line-height:34px}
.social i{width:25px;height:25px;border-radius:50%;display:block}
.rule{position:absolute;left:112px;top:1101px;width:975px;border-top:1px solid var(--line)}
.copy{position:absolute;left:0;width:1200px;top:1118px;text-align:center;font-size:12px;color:#555}
</style>
</head>
<body>
<div class="sheet">
  <div class="logo site-logo"><span class="logo-dot"></span><span class="logo-name">BK Services</span></div>
  <div class="account">
    <a href="#"><svg width="10" height="12" viewBox="0 0 10 12"><rect x="1" y="5" width="8" height="7" fill="#fff"/><path d="M2.5 5V3.5a2.5 2.5 0 0 1 5 0V5" stroke="#fff" fill="none" stroke-width="1.5"/></svg>Login</a>
    <a href="#"><svg width="12" height="12" viewBox="0 0 12 12"><circle cx="8" cy="4" r="3" fill="#fff"/><path d="M6 6L1 11" stroke="#fff" stroke-width="2"/></svg>Register</a>
  </div>
  <div class="call"><span>CALL NOW:</span> +91-55520 41830</div>

  <nav class="nav"><a href="#">HOME</a><a href="#">ABOUT US</a><a href="#">SERVICES</a><a href="#">INSPIRE</a><a href="#">CONTACT US</a></nav>

  <div class="hero">
    <div class="hero-photo" role="img" aria-label="Photo of a smiling consultant in a bright office with colleagues blurred behind"></div>
    <div class="hero-tag"><h2>SIMPLE THINGS</h2><p>lead to greater heights!</p></div>
    <div class="wheel" role="img" aria-label="Quality assurance lifecycle wheel illustration"></div>
  </div>

  <div class="news">
    <div class="news-label">News</div>
    <div class="news-text">Lorem Ipsum is simply dummy text of the printing and typesetting industry.</div>
    <div class="news-arrows"><span>&#8249;</span><span>&#8250;</span></div>
  </div>

  <div class="service" style="left:27px">
    <div class="service-art" role="img" aria-label="Illustration of a team meeting in front of a chart board" style="background:linear-gradient(135deg,#e8e8e8,#d8a070);border-radius:6px"></div>
    <h3>Our Services</h3>
    <p>Lorem Ipsum is simply dummy text of the printing and typesetting.</p>
  </div>
  <div class="service" style="left:339px">
    <div class="service-art" role="img" aria-label="Illustration of colourful rising bars with a figure climbing" style="background:linear-gradient(90deg,#e8b020,#40a040,#2070c0,#d03020);border-radius:4px"></div>
    <h3 style="top:20px">Inspire</h3>
    <p>Lorem Ipsum is simply dummy text of the printing and typesetting.</p>
  </div>
  <div class="service" style="left:651px">
    <div class="service-art" role="img" aria-label="Colourful circular puzzle emblem" style="background:radial-gradient(circle,#f0f0f0 0 15%,#90c030 45%,#20b0a0 100%);border-radius:50%"></div>
    <h3>ICT Sourcing</h3>
    <p>Lorem Ipsum is simply dummy text of the printing and typesetting.</p>
  </div>

  <div class="panel" style="left:27px">
    <div class="panel-head" style="background:var(--brand)">About Us
      <svg width="24" height="24" viewBox="0 0 24 24"><circle cx="12" cy="12" r="11" fill="#fff"/><circle cx="12.5" cy="6.5" r="1.8" fill="#0b6ab8"/><path d="M10 10h3.5v8H10z" fill="#0b6ab8"/></svg>
    </div>
    <div class="panel-body">
      <p>Lorem Ipsum is simply dummy text of the printing and typesetting industry. Lorem Ipsum has been the industry's standard dummy text ever since the 1500s, when an unknown .</p>
      <p>printer took a galley of type and scrambled it to make a type specimen book. It has survived not only five centuries, but also the leap into electronic typesetting.</p>
    </div>
  </div>
  <div class="panel" style="left:340px">
    <div class="panel-head" style="background:var(--events-red)">Events
      <svg width="24" height="24" viewBox="0 0 24 24"><rect x="2" y="3" width="20" height="19" fill="none" stroke="#fff" stroke-width="2"/><rect x="2" y="3" width="20" height="5" fill="#fff"/><g fill="#fff"><rect x="5" y="11" width="3" height="3"/><rect x="10.5" y="11" width="3" height="3"/><rect x="16" y="11" width="3" height="3"/><rect x="5" y="16" width="3" height="3"/><rect x="10.5" y="16" width="3" height="3"/><rect x="16" y="16" width="3" height="3"/></g></svg>
    </div>
    <div class="panel-body">
      <div class="date">Oct. 25, 2013</div>
      <div>Lorem Ipsum is simply dummy text of the printing and typesetting industry.</div>
      <div class="more" style="margin-top:2px">Read More</div>
      <div class="date" style="margin-top:6px">Oct. 25, 2013</div>
      <div>Lorem Ipsum is simply dummy text of the printing and typesetting industry.</div>
      <div class="more" style="margin-top:2px">Read More</div>
    </div>
  </div>
  <div class="panel" style="left:652px;width:299px">
    <div class="panel-head" style="background:var(--testimonial-grey)">Customer Testimonials
      <svg width="28" height="24" viewBox="0 0 28 24"><ellipse cx="11" cy="10" rx="10" ry="8" fill="#fff"/><path d="M5 15l-2 6 7-4z" fill="#fff"/><ellipse cx="19" cy="14" rx="8" ry="6" fill="#fff" stroke="#4a4a4a" stroke-width="1.5"/></svg>
    </div>
    <div class="panel-body">
      <div>Lorem Ipsum is simply dummy text of the printing and typesetting industry. Lorem Ipsum has been the industry's standard dummy.</div>
      <div class="who" style="margin-top:2px">Pieter, Leeds</div>
      <div style="margin-top:6px">Lorem Ipsum is simply dummy text of the printing and typesetting industry. Lorem Ipsum has been the industry's standard dummy.</div>
      <div class="who" style="margin-top:2px">Pieter, Leeds</div>
    </div>
  </div>
</div>

<div class="logo footer-logo"><span class="logo-dot"></span><span class="logo-name">BK Services</span></div>
<div class="fcol" style="left:307px;width:158px"><h4>About Us</h4><a href="#">Management profile</a><a href="#">Locations</a><a href="#">Careers</a><a href="#">Newsroom</a><a href="#">Partners</a></div>
<div class="fcol" style="left:465px;width:154px"><h4>BK Services</h4><a href="#">Management profile</a><a href="#">Locations</a><a href="#">Careers</a><a href="#">Newsroom</a><a href="#">Partners</a></div>
<div class="fcol" style="left:619px;width:153px;padding-left:24px"><h4>&nbsp;</h4><a href="#">Management profile</a><a href="#">Locations</a><a href="#">Careers</a><a href="#">Newsroom</a><a href="#">Partners</a></div>
<div class="fcol" style="left:772px;width:164px;padding-left:21px"><h4>Case Studies</h4><a href="#">Management profile</a><a href="#">Locations</a><a href="#">Careers</a><a href="#">Newsroom</a><a href="#">Partners</a></div>
<div class="fcol social" style="left:936px;width:151px;padding-left:25px"><h4>Follow Us</h4><a href="#"><i style="background:#3a5d96"></i>Facenote</a><a href="#"><i style="background:#3a8fd0"></i>Chirper</a><a href="#"><i style="background:#c84a3a"></i>Circles+</a></div>
<div class="rule"></div>
<div class="copy">© 2013 BK Services.All rights reserved.</div>
</body>
</html>
```